Brivora Australia Company Values.

We have just completed our company purpose, beliefs and values (for the first time, we have not had these before)
We are now wanting to add images to each company value as a visual
so they are easily identified and understood for all our staff - we need them to remember the 5 Values.
We are a manufacturer of dental materials and infection control products, based in Melbourne.

What we would like:
- A Poster (that can be placed in our staff lunch rooms)
- The values to be lined up Horizontally
- Image on the top of the words
- Wording does not all need to be the same text font
- No image photographs - please use image graphics
- No images with people
- No dental related graphics

Target audience: Brivora staff

Our Values are:
Think Big
Have a go, learn and adapt
If you're gonna do it, do it bloody well
Empower Others
Be a good human

I have uploaded some examples.

Target Market(s)

Brivora Team members

Industry/Entity Type

Healthcare

Colors

Designer to choose colors to be used in the design.

Requirements
Must have
• Clear horizontal layout, space between each value
Should not have
• No images with humans or dental

```html
<!DOCTYPE html>
<html lang="en">
<head>
<meta charset="utf-8">
<title>Brivora Australia – Company Values</title>
<link rel="stylesheet" href="https://fonts.googleapis.com/css2?family=Rubik:wght@700;800&family=Barlow+Condensed:wght@700&display=swap">
<style>
  :root{
    --bg:#333333;
    --paper:#ffffff;
    --green:#3fb846;
    --green-soft:#d9f0db;
    --navy:#172a5e;
    --rule:#c9c9c9;
    --display:"Rubik", Arial, sans-serif;
    --label:"Barlow Condensed", "Arial Narrow", sans-serif;
  }
  *{margin:0;padding:0;box-sizing:border-box}
  html,body{width:1200px;height:549px;overflow:hidden;background:var(--bg)}
  .canvas{position:relative;width:1200px;height:549px}

  .poster{position:absolute;left:106px;top:177px;width:988px;height:194px;background:var(--paper)}
  .poster-frame{position:absolute;left:8px;top:7px;right:8px;bottom:6px;border:12px solid var(--green)}

  .values-tab{position:absolute;left:0;top:32px;width:64px;height:131px;background:var(--navy);
    border-radius:0 16px 16px 0;display:flex;align-items:center;justify-content:center}
  .values-tab-text{transform:rotate(-90deg);display:flex;flex-direction:column;align-items:center;line-height:1;white-space:nowrap;color:var(--paper)}
  .values-tab-small{font-family:var(--display);font-weight:700;font-size:10px;letter-spacing:4.5px;order:2;margin-top:1px}
  .values-tab-big{font-family:var(--display);font-weight:800;font-size:32px;letter-spacing:-.5px;order:1}

  .divider{position:absolute;top:54px;height:88px;border-left:2px dashed var(--rule)}

  .value{position:absolute;top:0;height:194px;display:flex;flex-direction:column;align-items:center;color:var(--navy)}
  .value-icon{position:absolute;top:31px;width:58px;height:57px;border-radius:10px;background:var(--green-soft)}
  .value-words{position:absolute;top:92px;display:flex;flex-direction:column;align-items:center;white-space:nowrap;line-height:1}
  .display{font-family:var(--display);font-weight:800;letter-spacing:-.5px}
  .label{font-family:var(--label);font-weight:700;text-transform:uppercase;line-height:.95}
  .row{display:flex;align-items:flex-end;gap:5px}

  .v-think{left:88px;width:100px}
  .v-think .t1{font-size:24px;margin-top:-1px}
  .v-think .t2{font-size:60px;margin-top:-6px}

  .v-learn{left:202px;width:140px}
  .v-learn .pre{font-size:17px;margin-bottom:-3px}
  .v-learn .t1{font-size:36px}
  .v-learn .t2{font-size:36px;margin-top:-5px}

  .v-doit{left:368px;width:220px}
  .v-doit .pre{font-size:19px;text-align:left}
  .v-doit .t1{font-size:41px;margin-bottom:-5px}
  .v-doit .t2{font-size:41px;margin-top:-2px}

  .v-empower{left:614px;width:180px}
  .v-empower .t1{font-size:40px;margin-top:-2px}
  .v-empower .t2{font-size:40px;margin-top:-4px}

  .v-human{left:810px;width:150px}
  .v-human .pre{font-size:20px;margin-bottom:4px}
  .v-human .t1{font-size:42px;margin-top:-4px}
  .v-human .t2{font-size:42px;margin-top:-6px}
</style>
</head>
<body>
<main class="canvas">
  <section class="poster" aria-label="Brivora Australia company values">
    <div class="poster-frame"></div>

    <div class="values-tab">
      <div class="values-tab-text">
        <span class="values-tab-small">COMPANY</span>
        <span class="values-tab-big">VALUES</span>
      </div>
    </div>

    <article class="value v-think">
      <div class="value-icon" role="img" aria-label="Green line icon of a brain with spark lines"></div>
      <div class="value-words">
        <span class="display t1">Think</span>
        <span class="display t2">BIG</span>
      </div>
    </article>

    <span class="divider" style="left:193px"></span>

    <article class="value v-learn">
      <div class="value-icon" role="img" aria-label="Green line icon of an open book being read"></div>
      <div class="value-words">
        <span class="label pre">Have a go,</span>
        <span class="display t1">Learn &amp;</span>
        <span class="display t2">Adapt</span>
      </div>
    </article>

    <span class="divider" style="left:356px"></span>

    <article class="value v-doit">
      <div class="value-icon" style="width:68px" role="img" aria-label="Green icon of a celebratory high five"></div>
      <div class="value-words">
        <div class="row">
          <span class="label pre">If you're<br>gonna do it</span>
          <span class="display t1">Do It</span>
        </div>
        <span class="display t2">Bloody Well</span>
      </div>
    </article>

    <span class="divider" style="left:598px"></span>

    <article class="value v-empower">
      <div class="value-icon" style="width:48px" role="img" aria-label="Green line icon of a raised fist"></div>
      <div class="value-words">
        <span class="display t1">Empower</span>
        <span class="display t2">Others</span>
      </div>
    </article>

    <span class="divider" style="left:797px"></span>

    <article class="value v-human">
      <div class="value-icon" style="width:52px" role="img" aria-label="Green line icon of a thumbs up"></div>
      <div class="value-words">
        <div class="row">
          <span class="label pre">Be a</span>
          <span class="display t1">good</span>
        </div>
        <span class="display t2">human</span>
      </div>
    </article>
  </section>
</main>
</body>
</html>
```